To design a brand identity that is simple and creative with 'Valtor' as the brand name, I like modern simple fonts like helvetica neue, I want to print both sides of the card, I am open to dark front and white back, but the design needs to transfer well to letter heads and email signatures, I am looking for sophisticated and elegant, but open minded about clever and off the wall, I do not do 'boring' Valtor Holdings is the mother company for a small group, specialising in Management & consulting, Software development and construction, we have a high level of integrity, we are transparent and accountable for what we do. my images are provided as a guide only, Im not expecting them to be just copied, Im looking for a creator and passionate thinker, who will put life into their work.

Target Market(s)

usually business minded people who are looking for something different in me, such as leadership, confidence and focus with thinking that is per haps a little outside the box..

Industry/Entity Type

Construction

Requirements
Must have
• clean, minmalistic
Nice to have
• custom logo
Should not have
• boring, traditional

```html
<!DOCTYPE html>
<html lang="en">
<head>
<meta charset="utf-8">
<title>Valtor business card</title>
<link rel="stylesheet" href="https://fonts.googleapis.com/css2?family=Montserrat:ital,wght@0,300;0,400;1,300&display=swap">
<style>
  :root {
    --bg: #e6e6e7;
    --card: #ffffff;
    --orange: #ef7a1f;
    --ink: #2b2b2b;
    --grey: #8a8a8a;
    --shadow: rgba(0,0,0,0.12);
  }
  * { margin: 0; padding: 0; box-sizing: border-box; }
  html, body {
    width: 1200px; height: 947px; overflow: hidden;
    background: var(--bg);
    font-family: "Montserrat", Helvetica, Arial, sans-serif;
  }
  .stage {
    width: 1200px; height: 947px;
    display: flex; align-items: center; justify-content: center; gap: 60px;
  }
  .card {
    position: relative;
    width: 520px; height: 300px;
    background: var(--card);
    box-shadow: 0 8px 24px var(--shadow);
    overflow: hidden;
  }
  .card__stripe {
    position: absolute; left: 0; right: 0; bottom: 0;
    height: 7px; background: var(--orange);
  }
  .brand {
    display: flex; align-items: center; gap: 14px;
  }
  .brand__dot {
    width: 26px; height: 26px; border-radius: 50%;
    background: var(--orange);
    flex: none;
  }
  .brand__name {
    font-weight: 400; color: var(--ink);
    line-height: 1; letter-spacing: 0.18em;
    text-transform: uppercase;
  }
  .brand__tagline {
    font-weight: 400;
    color: var(--grey); letter-spacing: 0.5px;
  }

  /* front */
  .card--front .lockup {
    position: absolute; left: 50%; top: 50%;
    transform: translate(-50%, -58%);
  }
  .card--front .brand__name { font-size: 54px; }
  .card--front .brand__tagline {
    font-size: 15px; margin: 12px 0 0 40px;
  }

  /* back */
  .card--back .contact {
    position: absolute; left: 34px; top: 30px;
  }
  .contact__email { font-size: 19px; color: var(--orange); font-weight: 400; }
  .contact__role { font-size: 11px; color: var(--ink); margin-top: 3px; }
  .details {
    position: absolute; left: 34px; top: 110px;
    font-size: 14px; color: var(--ink); line-height: 1.55;
  }
  .details__label { color: var(--orange); }
  .details__sep { color: var(--orange); padding: 0 4px; }
  .card--back .lockup {
    position: absolute; right: 34px; bottom: 32px;
    text-align: right;
  }
  .card--back .brand { justify-content: flex-end; gap: 10px; }
  .card--back .brand__dot { width: 18px; height: 18px; }
  .card--back .brand__name { font-size: 32px; }
  .card--back .brand__tagline { font-size: 11px; margin-top: 6px; }
</style>
</head>
<body>
<main class="stage">
  <section class="card card--back" aria-label="Card back with contact details">
    <div class="contact">
      <p class="contact__email">marcus@valtor.holdings</p>
      <p class="contact__role">client ambassador</p>
    </div>
    <div class="details">
      <p><span class="details__label">M.</span> +61 0400 555 182</p>
      <p><span class="details__label">PO BOX</span> 418 Harbourton 6100</p>
      <p>management<span class="details__sep">•</span>software<span class="details__sep">•</span>construction</p>
    </div>
    <div class="lockup">
      <div class="brand">
        <span class="brand__dot"></span>
        <span class="brand__name">Valtor</span>
      </div>
      <p class="brand__tagline">..built with clear intent.</p>
    </div>
    <div class="card__stripe"></div>
  </section>

  <section class="card card--front" aria-label="Card front with brand name">
    <div class="lockup">
      <div class="brand">
        <span class="brand__dot"></span>
        <span class="brand__name">Valtor</span>
      </div>
      <p class="brand__tagline">..built with clear intent.</p>
    </div>
    <div class="card__stripe"></div>
  </section>
</main>
</body>
</html>
```